The Amber Lantern illustrated story adaptation design

I need a graphic-novel-style design of the 10-page story, “The Amber Lantern.” This will appear in a collection of graphic-novel-style adaptations of stories which I am posting online (and printing) in May.

Half of the files are on filecrate (under "6 images"):

https://www.filecrate-share.net/s/q3mz81kd0tx5pw2/page%20thumbs_0full_01.jpg?dl=0

Target Market(s)

comic book readers, graphic novel readers, young adult readers

Industry/Entity Type

Publishing

Font styles to use
Serif
Other font styles liked:
• Caslon Anitque, Californian FB, 1584 Pragmatica Lima

Colors

Designer to choose colors to be used in the design.

Requirements
Must have
• A bold design scheme !! The art and text are solid, but they certainly need a clever design concept that can bind the project together.
Nice to have
• An inviting, reader-friendly background of some kind (I offer suggestions in my notes).
Should not have
• Hard-to-read graphics

```html
<!DOCTYPE html>
<html lang="en">
<head>
<meta charset="utf-8">
<title>The Amber Lantern — Page 5</title>
<link rel="stylesheet" href="https://fonts.googleapis.com/css2?family=Crimson+Text:wght@600&family=IM+Fell+English&family=Old+Standard+TT:wght@400;700&display=swap">
<style>
  :root {
    --canvas: #ffffff;
    --stone-1: #8a8596;
    --stone-2: #a09aa8;
    --stone-3: #7d7890;
    --frame: #0b0b0d;
    --paper: #dcd6de;
    --paper-2: #cfc8d3;
    --ink: #141216;
    --header: #f4f1f6;
    --art-dark-1: #1c1638;
    --art-dark-2: #3b2c78;
    --art-dark-3: #231a45;
    --art-lit-1: #2a2360;
    --art-lit-2: #4a5fb0;
    --art-lit-3: #a03a8a;
  }
  * { margin: 0; padding: 0; box-sizing: border-box; }
  html, body { width: 1200px; height: 1200px; overflow: hidden; background: var(--canvas); }
  .canvas { position: relative; width: 1200px; height: 1200px; }
  .page {
    position: absolute; left: 172px; top: 68px; width: 856px; height: 1062px;
    background:
      radial-gradient(ellipse at 30% 40%, rgba(180,150,190,.35), transparent 60%),
      radial-gradient(ellipse at 80% 70%, rgba(120,115,140,.4), transparent 55%),
      linear-gradient(160deg, var(--stone-2), var(--stone-1) 50%, var(--stone-3));
  }
  .running-head {
    position: absolute; top: 52px; font-family: "Crimson Text", serif; font-weight: 600;
    font-size: 21px; color: var(--header); line-height: 1;
  }
  .page-number { left: 62px; }
  .story-title { right: 62px; }
  .panel { position: absolute; border: 10px solid var(--frame); }
  .panel-text {
    background: linear-gradient(135deg, var(--paper), var(--paper-2));
    font-family: "Old Standard TT", serif; color: var(--ink);
  }
  .panel-intro { left: 65px; top: 108px; width: 375px; height: 246px; padding: 10px 14px; font-size: 16.5px; line-height: 21px; }
  .panel-intro p { margin-bottom: 17px; }
  .drop-cap {
    float: left; font-family: "IM Fell English", serif; font-size: 52px; line-height: 40px;
    margin: 2px 6px 0 0; font-weight: 700;
  }
  .panel-intro .shout { font-size: 25px; font-weight: 700; line-height: 28px; margin-top: 6px; }
  .panel-art-charge {
    left: 431px; top: 108px; width: 361px; height: 404px;
    background: radial-gradient(ellipse at 55% 45%, var(--art-dark-2), var(--art-dark-3) 60%, var(--art-dark-1));
  }
  .panel-art-warrior {
    left: 65px; top: 532px; width: 375px; height: 464px;
    background:
      radial-gradient(ellipse at 50% 55%, var(--art-lit-2), transparent 55%),
      radial-gradient(ellipse at 25% 55%, var(--art-lit-3), transparent 40%),
      linear-gradient(180deg, var(--art-dark-1), var(--art-lit-1));
  }
  .panel-combat {
    left: 431px; top: 650px; width: 381px; height: 346px;
    padding: 34px 14px 0 30px; font-size: 16.5px; line-height: 21px;
  }
</style>
</head>
<body>
<div class="canvas">
  <main class="page">
    <div class="running-head page-number">Page 5</div>
    <div class="running-head story-title">The Amber Lantern</div>

    <section class="panel panel-text panel-intro">
      <p><span class="drop-cap">W</span>ith a low laugh, he stepped into the center of the passageway.</p>
      <p>“Come, brothers,” he bellowed. He banged his blade against the stone wall. “Here is better sport.”</p>
      <p class="shout">He rushed the soldiers.</p>
    </section>

    <div class="panel panel-art-charge" role="img" aria-label="Painted silhouette of the warrior charging forward with a shield through a dark violet corridor"></div>

    <div class="panel panel-art-warrior" role="img" aria-label="Painted armored warrior standing with sword lowered amid blue and magenta light in a stone passage"></div>

    <section class="panel panel-text panel-combat">
      <p>The sword in his hand flashed: he gutted the largest member of the guard. Before that body struck the stone floor, his gleaming blade severed the second man’s head: the third he grabbed by the neck and, lifting a corded arm, snapped the man’s neck. The fourth and fifth guardsmen held back. He motioned for them to advance. They fled. Snatching a blade from the dead man, he flung it and saw the fourth man fall gurgling to the stone floor.</p>
    </section>
  </main>
</div>
</body>
</html>
```